Wordpress Design For Financial Investment Company

//** NEW WIREFRAME ADDED TO HELP WITH LAYOUT ISSUES. PLEASE REFER TO WIREFRAME IN ATTACHED FILES. NO DESIGN WILL BE CONSIDERED IF IT DOES NOT FOLLOW THE WIREFRAME. **//
//** PLEASE READ THE ENTIRE BRIEF INCLUDING ALL UPDATES TO THE BRIEF. THE CLIENT IS VERY SPECIFIC ABOUT WHAT THEY WANT AND I'VE COVERED SEVERAL THINGS IN THE UPDATES. THERE IS ALSO A VIDEO UPDATE THAT HAS SOME VALUABLE INFORMATION IN IT FOR THIS CONTEST. **//
The client is an investment advisor who needs a new website designed. The current site is http://www.veltorbay.net.
The client wants the site to be green to match the attached logo.
The home page should have relevant images in the rotator. No people hugging! This is a financial investment site, not a family counseling site.
Also, the client wants 4 buttons on the home page to highlight the 4 main areas they focus on:
Investment Advice and Education
General Financial Planning
Retirement Planning
401K Planning
The top right area of the site needs to have their phone number, a call to action, and 2 buttons.
Their phone number is 303-481-7294
The call to action should say something like "Call for a free consultation!"
The buttons need to say:
Login To Your Quellbrook Account
Login To Your Halvenpoint Account
The final design should communicate professionalism, financial safety and growth.
Main navigation should be:
Home
About Us
Associates
Services
Contact
Mission Statement (Could also be "Our Mission")
This is a site that the client likes: http://www.pmrwealthguidance.com/
Updates
The designs should not have:
Newsletter content. A newsletter sign up is fine
Learning Center
Calculators
Stock prices/tickers
The design should have a contact form on the page.
I have talked to my client and have some updates. I did a video update because I thought it would be easier to show what I'm trying to get across.
Reason: I am going to be extending the contest a few more days. I'm still not getting quite what I want and very few people are even trying to follow the creative brief and the updates to it.
PLEASE read the entire brief and the updates. There is also a video I made that explains everything. I've also attached a wireframe.
Thanks!
Target Market(s)
People looking for a high-end financial investment company.
Industry/Entity Type
Investment
Requirements
Must have
- !!FOLLOW THE WIREFRAME FOR LAYOUT!!
!!THEIR LOGO!!
4 buttons to highlight their main practice areas
Phone number in the top right
"Free Consultation" call to action
2 Login buttons in the top right
A contact form on the page.
Should not have
- The designs should not have:
Learning Center
Calculators
Stock prices/tickers

```html
<!DOCTYPE html>
<html lang="en">
<head>
<meta charset="utf-8">
<title>Veltorbay Financial Consultancy</title>
<link rel="stylesheet" href="https://fonts.googleapis.com/css2?family=Roboto:wght@300;400;500&family=Arimo:ital,wght@0,400;0,700;1,400&display=swap">
<style>
:root{
  --green-dark:#213a27;
  --green:#2e4d35;
  --green-mid:#3e6748;
  --green-btn:#5d8a66;
  --cream:#f3e6d4;
  --cream-light:#fdf2e2;
  --tan:#e5cfae;
  --tan-dark:#b79a72;
  --ink:#2f4a35;
  --text:#5c5a55;
  --grey-btn:#d9d9d6;
  --footer:#1e2a20;
  --footer-bar:#141a15;
  --link:#7fbf8a;
  --white:#ffffff;
}
*{box-sizing:border-box;margin:0;padding:0}
html,body{width:690px;height:1200px;overflow:hidden;background:var(--white)}
body{position:relative;font-family:"Arimo",Arial,sans-serif;color:var(--text);font-size:7px}
.abs{position:absolute}
h2,.heading{font-family:"Roboto",Arial,sans-serif;font-weight:400;color:var(--ink);text-transform:uppercase}
p.body{font-size:7.2px;line-height:11px;text-align:justify;color:var(--text)}

/* header */
.site-header{position:absolute;left:0;top:0;width:690px;height:74px;background:linear-gradient(var(--green-mid),var(--green-dark))}
.brand{position:absolute;left:10px;top:6px;width:84px;text-align:center}
.brand-mark{width:52px;height:52px;border-radius:50%;background:var(--tan);margin:0 auto;display:flex;align-items:center;justify-content:center;border:2px solid #8a6d48}
.brand-name{font-family:"Roboto",sans-serif;font-weight:500;font-size:9px;color:var(--green-dark)}
.brand-tag{font-size:8px;color:var(--tan);margin-top:3px;white-space:nowrap}
.main-nav{position:absolute;left:100px;top:29px;display:flex;height:28px}
.main-nav a{font-family:"Arimo",sans-serif;font-size:8px;color:var(--white);text-decoration:none;padding:0 13px;line-height:28px;white-space:nowrap}
.main-nav a.active{background:var(--tan);color:var(--green-dark)}
.login{position:absolute;top:6px;width:90px;height:24px;border:1px solid #9db8a2;border-radius:2px;background:var(--green);color:var(--white);font-size:7px;line-height:8px;padding:3px 0 0 22px;white-space:nowrap}
.login svg{position:absolute;left:6px;top:6px}
.call-box{position:absolute;left:494px;top:42px;width:186px;height:23px;background:var(--cream);border-radius:3px;display:flex;align-items:center;padding-left:6px;gap:5px;color:var(--green-dark);white-space:nowrap;overflow:hidden}
.call-box .cta{font-size:6.8px;font-weight:700}
.call-box .num{font-family:"Roboto",sans-serif;font-size:11px;font-weight:500;margin-left:2px}

/* hero */
.hero{position:absolute;left:7px;top:85px;width:674px;height:292px;background:var(--cream);border:1px solid #cbb99e;border-radius:3px;overflow:hidden}
.hero-photo{position:absolute;left:5px;top:6px;width:365px;height:218px;background:linear-gradient(160deg,#8a7a3e 0%,#b08b45 35%,#6f6a30 60%,#4f6a2a 100%)}
.hero h1{position:absolute;left:411px;top:14px;font-family:"Roboto",sans-serif;font-weight:400;font-size:26px;color:var(--ink);white-space:nowrap}
.hero p.body{position:absolute;left:411px;top:66px;width:252px}
.btn-outline{position:absolute;top:177px;height:18px;border:1px solid #a69b8a;border-radius:3px;background:#f8efe2;font-size:7.5px;line-height:16px;text-align:center;color:var(--green-dark);white-space:nowrap}
.focus-bar{position:absolute;left:0;top:229px;width:674px;height:63px;background:var(--green);display:flex}
.focus-item{flex:1;border-right:1px solid #1b2f20;display:flex;align-items:center;gap:12px;padding-left:9px;color:var(--white);font-family:"Roboto",sans-serif;font-size:9.5px;line-height:11px;text-transform:uppercase}
.focus-item:last-child{border-right:0}
.focus-icon{width:37px;height:37px;background:var(--cream);border-radius:3px;display:flex;align-items:center;justify-content:center;flex:none}

/* columns */
.col{position:absolute;top:404px;width:149px}
.col h2{font-size:11.5px;margin-bottom:9px;white-space:nowrap}
.col .photo{width:149px;height:72px;border:1px solid #999;border-radius:3px;background:linear-gradient(#eeeeee,#bdbdbd)}
.col p.body{margin-top:10px;height:64px;overflow:hidden}
.btn-grey{display:block;margin-top:15px;width:62px;height:18px;border-radius:3px;background:var(--grey-btn);font-size:7.5px;line-height:18px;text-align:center;color:#444}
.btn-grey.on{background:var(--green);color:var(--white)}
.dash-rule{position:absolute;left:0;top:635px;width:690px;border-top:1px dashed #8a9a8d}

/* news + testimonials */
.lower-head{position:absolute;top:665px;font-size:11.5px}
.news-item{position:absolute;left:7px;width:149px;height:80px}
.date{position:absolute;left:0;top:0;width:40px;height:33px;background:var(--green-mid);border-radius:4px;color:var(--white);text-align:center;font-family:"Roboto",sans-serif}
.date b{display:block;font-size:14px;font-weight:500;margin-top:3px;line-height:15px}
.date span{font-size:8px}
.news-item p.body{position:absolute;left:47px;top:0;width:102px;height:44px;overflow:hidden}
.more{position:absolute;right:0;top:44px;font-size:7.5px;line-height:9px;font-style:italic;text-decoration:underline;color:#444}
.news-rule{position:absolute;left:7px;width:149px;border-top:1px solid #c9c9c9}
.v-dots{position:absolute;left:181px;top:693px;height:225px;border-left:1px dotted #777}
.quote{position:absolute;left:208px;width:149px}
.quote .who{text-align:right;font-style:italic;font-size:7px;margin-top:2px;color:#444}
.quote-rule{position:absolute;left:208px;width:149px;border-top:1px dotted #777}

/* contact form */
.contact-box{position:absolute;left:437px;top:666px;width:243px;height:252px;background:var(--cream-light);border-radius:4px}
.contact-box h2{position:absolute;left:61px;top:8px;font-size:11.5px}
.contact-box label{position:absolute;left:15px;font-size:7.5px;color:#444}
.field{position:absolute;left:79px;width:148px;height:19px;border:1px solid #8b7b65;border-radius:2px;background:#f7ead6}
.btn-green{position:absolute;left:164px;top:229px;width:62px;height:18px;border-radius:3px;background:linear-gradient(var(--green-btn),var(--green-mid));color:var(--white);font-size:7.5px;line-height:18px;text-align:center}

/* newsletter */
.news-line{position:absolute;left:0;top:955px;width:690px;border-top:1px solid #c8c3b8}
.newsletter{position:absolute;left:269px;top:944px;width:149px;height:24px;border:1px solid #c8c3b8;border-radius:12px;background:var(--white);font-size:8px;color:var(--green-dark);line-height:22px;padding-left:44px;white-space:nowrap}
.newsletter svg{position:absolute;left:10px;top:5px}

/* footer */
.site-footer{position:absolute;left:0;top:992px;width:690px;height:181px;background:var(--footer)}
.foot-col{position:absolute;top:13px}
.foot-col h3{font-family:"Roboto",sans-serif;font-weight:400;font-size:11.5px;color:var(--white);margin-bottom:11px;white-space:nowrap}
.foot-col ul{list-style:none}
.foot-col li{font-size:7.5px;line-height:10.7px;color:var(--link)}
.foot-text{color:var(--white);font-size:7.5px;line-height:10.5px;white-space:nowrap}
.social{position:absolute;left:530px;top:38px;display:flex;gap:10px}
.social span{width:31px;height:26px;border-radius:50%;background:var(--tan)}
.foot-brand{position:absolute;left:530px;top:88px;display:flex;align-items:center;gap:5px}
.foot-brand .dot{width:32px;height:32px;border-radius:50%;background:var(--tan);flex:none}
.foot-brand .name{font-family:"Roboto",sans-serif;font-size:20px;font-weight:400;color:var(--white);line-height:19px}
.foot-brand .sub{font-family:"Roboto",sans-serif;font-size:11px;color:var(--white);white-space:nowrap}
.copyright{position:absolute;left:0;top:1173px;width:690px;height:27px;background:var(--footer-bar);color:#ddd;text-align:center;font-size:7.5px;line-height:20px}
</style>
</head>
<body>

<header class="site-header">
  <div class="brand">
    <div class="brand-mark"><span class="brand-name">Veltorbay</span></div>
    <div class="brand-tag">Financial Consultancy</div>
  </div>
  <nav class="main-nav">
    <a href="#">Home</a><a href="#">About us</a><a href="#">Associate</a><a href="#" class="active">Services</a><a href="#">Our Mission</a><a href="#">Contact us</a>
  </nav>
  <div class="login" style="left:494px">
    <svg width="10" height="11" viewBox="0 0 10 11"><rect x="1" y="4" width="8" height="7" fill="#e5cfae"/><path d="M3 4V2.5a2 2 0 0 1 4 0V4" stroke="#e5cfae" fill="none" stroke-width="1.3"/></svg>
    Login for your<br>Quellbrook account
  </div>
  <div class="login" style="left:590px">
    <svg width="10" height="11" viewBox="0 0 10 11"><rect x="1" y="4" width="8" height="7" fill="#e5cfae"/><path d="M3 4V2.5a2 2 0 0 1 4 0V4" stroke="#e5cfae" fill="none" stroke-width="1.3"/></svg>
    Login for your<br>Halvenpoint account
  </div>
  <div class="call-box">
    <svg width="16" height="12" viewBox="0 0 16 12"><path d="M1 4c0-2 3-3 7-3s7 1 7 3v1h-4V3.5H5V5H1z" fill="#213a27"/><rect x="3" y="6" width="10" height="5" rx="1" fill="#213a27"/></svg>
    <span class="cta">Call us for Free Consulation</span><span class="num">303 481 7294</span>
  </div>
</header>

<section class="hero">
  <div class="hero-photo" role="img" aria-label="Photo of an autumn park with a wooden bench under a large tree"></div>
  <h1>RETIREMENT PLAN</h1>
  <p class="body">Lorem Ipsum is simply dummy text of the printing and typesetting industry. Lorem Ipsum has been the industry's standard dummy text ever since the 1500s, when an unknown printer took a galley of type and scrambled it to make a type specimen book. It has survived not only five centuries, but also the leap into electronic typesetting, remaining essentially unchanged. It was popularised in the 1960s with the release of Letraset sheets containing Lorem Ipsum passages, and more recently with desktop publishing software like Aldus PageMaker including versions of Lorem Ipsum.</p>
  <span class="btn-outline" style="left:411px;width:62px">Learn more</span>
  <span class="btn-outline" style="left:480px;width:62px">Call us Now</span>
  <div class="focus-bar">
    <div class="focus-item">
      <div class="focus-icon"><svg width="24" height="22" viewBox="0 0 24 22"><g fill="#5d8a66"><ellipse cx="12" cy="18" rx="9" ry="3"/><ellipse cx="12" cy="13" rx="9" ry="3"/><ellipse cx="12" cy="8" rx="9" ry="3"/><ellipse cx="12" cy="4" rx="9" ry="3" fill="#7fa886"/></g></svg></div>
      <span>Investment advice<br>and education</span>
    </div>
    <div class="focus-item">
      <div class="focus-icon"><svg width="22" height="22" viewBox="0 0 22 22"><rect x="1" y="2" width="20" height="19" fill="none" stroke="#2e4d35" stroke-width="1.5"/><rect x="1" y="2" width="20" height="4" fill="#5d8a66"/><text x="11" y="17" font-size="9" text-anchor="middle" font-family="Arimo,sans-serif" font-weight="700" fill="#2e4d35">14</text></svg></div>
      <span>General financial<br>planning</span>
    </div>
    <div class="focus-item">
      <div class="focus-icon"><svg width="22" height="22" viewBox="0 0 22 22"><rect x="2" y="2" width="18" height="18" rx="2" fill="#2e4d35"/><path d="M11 6l4 4-4 7-4-7z" fill="#e5cfae"/></svg></div>
      <span>Retirement<br>plan</span>
    </div>
    <div class="focus-item">
      <div class="focus-icon"><svg width="22" height="22" viewBox="0 0 22 22"><rect x="2" y="2" width="17" height="19" fill="none" stroke="#2e4d35" stroke-width="1.5"/><rect x="2" y="2" width="17" height="4" fill="#5d8a66"/><path d="M7 17l9-9 2 2-9 9H7z" fill="#5d8a66"/></svg></div>
      <span>401 K<br>planing</span>
    </div>
  </div>
</section>

<div class="col" style="left:7px">
  <h2>About us</h2>
  <div class="photo" role="img" aria-label="Black and white portrait of a businessman in glasses"></div>
  <p class="body">Lorem Ipsum is simply dummy text of the printing and typesetting industry. Lorem Ipsum has been the industry's standard dummy text ever since the 1500s, when an unknown printer took a galley of type and scrambled it to make a type specimen book. It</p>
  <span class="btn-grey">Learn more</span>
</div>
<div class="col" style="left:181px">
  <h2>Why custmer chose us</h2>
  <div class="photo" role="img" aria-label="Black and white portrait of a smiling businesswoman"></div>
  <p class="body">Lorem Ipsum is simply dummy text of the printing and typesetting industry. Lorem Ipsum has been the industry's standard dummy text ever since the 1500s, when an unknown printer took a galley of type and scrambled it to make a type specimen book. It</p>
  <span class="btn-grey">Learn more</span>
</div>
<div class="col" style="left:357px">
  <h2>Our mission</h2>
  <div class="photo" role="img" aria-label="Black and white photo of a business team looking upward"></div>
  <p class="body">Lorem Ipsum is simply dummy text of the printing and typesetting industry. Lorem Ipsum has been the industry's standard dummy text ever since the 1500s, when an unknown printer took a galley of type and scrambled it to make a type specimen book. It</p>
  <span class="btn-grey">Learn more</span>
</div>
<div class="col" style="left:530px">
  <h2>Support</h2>
  <div class="photo" role="img" aria-label="Black and white photo of a support agent in glasses"></div>
  <p class="body">Lorem Ipsum is simply dummy text of the printing and typesetting industry. Lorem Ipsum has been the industry's standard dummy text ever since the 1500s, when an unknown printer took a galley of type and scrambled it to make a type specimen book. It</p>
  <span class="btn-grey on">Learn more</span>
</div>

<div class="dash-rule"></div>

<h2 class="lower-head" style="left:7px">Latest news</h2>
<div class="news-item" style="top:695px">
  <div class="date"><b>28</b><span>Feb</span></div>
  <p class="body">Lorem Ipsum is simply dummy text of the printing and typeset-ting industry. Lorem Ipsum has been the industry's standard</p>
  <span class="more">Learn more</span>
</div>
<div class="news-rule" style="top:757px"></div>
<div class="news-item" style="top:782px">
  <div class="date"><b>28</b><span>Feb</span></div>
  <p class="body">Lorem Ipsum is simply dummy text of the printing and typeset-ting industry. Lorem Ipsum has been the industry's standard</p>
  <span class="more">Learn more</span>
</div>
<div class="news-rule" style="top:843px"></div>
<div class="news-item" style="top:868px">
  <div class="date"><b>28</b><span>Feb</span></div>
  <p class="body">Lorem Ipsum is simply dummy text of the printing and typeset-ting industry. Lorem Ipsum has been the industry's standard</p>
  <span class="more">Learn more</span>
</div>

<div class="v-dots"></div>

<h2 class="lower-head" style="left:208px">Testimonials</h2>
<div class="quote" style="top:693px"><p class="body">Lorem Ipsum is simply dummy text of the printing and typesetting industry. Lorem Ipsum has been the industry's standard dummy text ever since the 1500s, when an</p><div class="who">Mr Parker</div></div>
<div class="quote-rule" style="top:757px"></div>
<div class="quote" style="top:779px"><p class="body">Lorem Ipsum is simply dummy text of the printing and typesetting industry. Lorem Ipsum has been the industry's standard dummy text ever since the 1500s, when an</p><div class="who">Mr Parker</div></div>
<div class="quote-rule" style="top:843px"></div>
<div class="quote" style="top:866px"><p class="body">Lorem Ipsum is simply dummy text of the printing and typesetting industry. Lorem Ipsum has been the industry's standard dummy text ever since the 1500s, when an</p><div class="who">Mr Parker</div></div>

<section class="contact-box">
  <svg class="abs" style="left:15px;top:5px" width="31" height="19" viewBox="0 0 31 19"><rect x="0.5" y="0.5" width="30" height="18" rx="2" fill="#b79a72" stroke="#8a6d48"/><path d="M1 1l14.5 10L30 1" fill="none" stroke="#8a6d48"/></svg>
  <h2>Contact us</h2>
  <label style="top:51px">Name *</label><div class="field" style="top:45px"></div>
  <label style="top:79px">Last Name *</label><div class="field" style="top:74px"></div>
  <label style="top:110px">Email *</label><div class="field" style="top:104px"></div>
  <label style="top:139px">Comapny *</label><div class="field" style="top:134px"></div>
  <label style="top:168px">Message *</label><div class="field" style="top:165px;height:53px"></div>
  <span class="btn-green">Learn more</span>
</section>

<div class="news-line"></div>
<div class="newsletter">
  <svg width="20" height="14" viewBox="0 0 20 14"><rect x="1" y="1" width="18" height="12" fill="#d9d9d6" stroke="#888"/><path d="M4 4h12M4 7h12M4 10h8" stroke="#888"/></svg>
  NEWSLETTER SIGN UP
</div>

<footer class="site-footer">
  <div class="foot-col" style="left:7px">
    <h3>QUICK LINKS</h3>
    <ul><li>Home</li><li>About us</li><li>Services</li><li>Associate</li><li>Our &nbsp;mission</li><li>Contact us</li><li>Privacy policy</li><li>Terms of use</li><li>Site map</li></ul>
  </div>
  <div class="foot-col" style="left:182px">
    <h3>SERVICES</h3>
    <ul><li>Services 1</li><li>Services 2</li><li>Services 3</li><li>Services 4</li><li>Services5</li><li>Services6</li><li>Services7</li></ul>
  </div>
  <div class="foot-col" style="left:356px">
    <h3>CONTACT US</h3>
    <div class="foot-text" style="font-size:11px;margin-bottom:8px">Address :</div>
    <div class="foot-text">Comapny Address Goes Herea:</div>
    <div class="foot-text" style="margin-top:29px">Phone : 303-481-7350<br>Email : info@veltorbay.net</div>
  </div>
  <div class="foot-col" style="left:530px"><h3>SOCIAL MEDIA LINKS</h3></div>
  <div class="social"><span></span><span></span><span></span></div>
  <div class="foot-brand">
    <span class="dot"></span>
    <div><div class="name">VELTORBAY</div><div class="sub">Financial Consultant</div></div>
  </div>
</footer>
<div class="copyright">All Copyright reserved by comapny name</div>

</body>
</html>
```